Photo Scanning New Business, Needs flyer design to capture Christmas gift ideas

Need a A5 size flyer for our business. Were a new business offering photo scanning and just about to go online. customers send us their old photos, slides or negatives from under their beds or in their cupboards and we then scan and digitize them and place onto a dvd or usb stick so they can view on their tv or computer anytime anywhere. Scanning old pictures isnt new bt very time consuming. Many customers like to download their photos from their digital cameras onto different social media websites, but their old photos they cant. Old photos also degrade and can get damaged.

I have included a design i was messing around with, which gives you the concept and wording im trying to get across in this flyer.

Target Market(s)

35 years and older. family members

Industry/Entity Type

Computer

Requirements
Must have
• the add must show the offer of "500 photos scanned for $50.00 Only"
Also have some words around " Make a great Christmas gift"

Needs to describe what the business is about
Nice to have
• please see my a5 flyer deisgn. colourful pictures. the flyer will be aimed at the christmas market, and hoping that people look at this and think that $50 is not alot of money for a christmas gift for one of the family, and that having all their pictures scanned is actually a good idea. Keeps them safe from Fire, Flood and Damage.
Should not have
• should not use cartoon style design

```html
<!DOCTYPE html>
<html lang="en">
<head>
<meta charset="utf-8">
<title>RetroDigi Christmas Scanning Flyer</title>
<link rel="stylesheet" href="https://fonts.googleapis.com/css2?family=Alfa+Slab+One&family=Arvo:wght@700&family=Roboto:wght@500;700&display=swap">
<style>
  :root {
    --navy: #1d4a86;
    --navy-deep: #163c70;
    --orange: #ee6a1a;
    --orange-bright: #f5821f;
    --white: #ffffff;
    --paper: #f4f4f6;
    --sepia: #b9a78a;
    --sepia-dark: #6e6352;
  }
  * { box-sizing: border-box; margin: 0; padding: 0; }
  html, body { width: 839px; height: 1200px; overflow: hidden; background: var(--white); }
  .flyer { position: relative; width: 839px; height: 1200px; overflow: hidden; background: var(--white); font-family: "Arvo", Georgia, serif; }

  .top-rule { position: absolute; left: 0; top: 0; width: 839px; height: 22px; background: var(--navy); }
  .headline-band { position: absolute; left: 0; top: 22px; width: 839px; height: 66px; background: var(--orange);
    display: flex; align-items: center; justify-content: center; }
  .headline { color: var(--white); font-size: 31px; letter-spacing: 0.5px; }

  .hero-zone { position: absolute; left: 0; top: 88px; width: 839px; height: 809px;
    background: radial-gradient(ellipse at 45% 70%, #ffffff 0%, #f6f6f8 60%, #ececf0 100%); }

  .photo { position: absolute; border: 5px solid var(--white); box-shadow: 2px 3px 8px rgba(0,0,0,0.35); }
  .photo--slides { left: -10px; top: 92px; width: 175px; height: 520px; transform: rotate(-3deg);
    background: linear-gradient(170deg, #e9e3d3 0%, #a9a294 35%, #8f7c68 55%, #c8c3b8 80%, #9a968f 100%); }
  .photo--old-top { left: 570px; top: 90px; width: 175px; height: 120px; transform: rotate(-2deg);
    background: linear-gradient(160deg, var(--sepia) 0%, #8f7b60 100%); }
  .photo--portraits { left: 700px; top: 130px; width: 160px; height: 430px; transform: rotate(4deg);
    background: linear-gradient(180deg, #9c8f7c 0%, #4b4640 40%, #7e7468 70%, #cbc3b8 100%); }
  .photo--film { left: 560px; top: 230px; width: 90px; height: 80px; transform: rotate(-30deg);
    background: linear-gradient(90deg, #7a2a0d, #d8621e, #7a2a0d); border: none; }
  .photo--children { left: 30px; top: 475px; width: 620px; height: 400px; border: none; box-shadow: none;
    background: radial-gradient(ellipse at 45% 50%, #f0ded3 0%, #e6d4c8 30%, #c9c9cd 60%, rgba(240,240,244,0) 80%); }

  .service-line { position: absolute; left: 170px; top: 118px; width: 500px; text-align: center;
    color: var(--navy); font-size: 27px; line-height: 1.2; }

  .offer-count { position: absolute; left: 95px; top: 205px; font-family: "Alfa Slab One", Georgia, serif;
    font-size: 128px; line-height: 1; color: var(--orange); transform: rotate(-8deg);
    -webkit-text-stroke: 2px var(--white); text-shadow: 3px 4px 0 var(--navy-deep); }
  .offer-band { position: absolute; left: 168px; top: 322px; width: 390px; height: 62px; background: var(--navy);
    transform: rotate(-8deg); display: flex; align-items: center; justify-content: center; }
  .offer-band span { color: var(--orange-bright); font-size: 35px; }

  .price-band { position: absolute; left: 297px; top: 380px; width: 268px; height: 58px; background: var(--orange);
    display: flex; align-items: center; justify-content: center; }
  .price-band span { color: var(--navy); font-size: 35px; }
  .price { position: absolute; left: 458px; top: 398px; font-family: "Alfa Slab One", Georgia, serif;
    color: var(--navy); font-size: 140px; line-height: 1; -webkit-text-stroke: 2px var(--white);
    text-shadow: 0 0 14px rgba(238,106,26,0.7); }
  .price small { font-size: 70px; vertical-align: 18px; }

  .gift-line { position: absolute; left: 440px; top: 552px; width: 380px; text-align: center;
    color: var(--navy); font-size: 32px; line-height: 1.25; -webkit-text-stroke: 0.5px var(--white); }

  .pickup-note { position: absolute; left: 545px; top: 752px; width: 285px; text-align: center;
    color: var(--navy); font-size: 20px; line-height: 1.3; }
  .pickup-note em { font-style: normal; color: var(--orange); }

  .benefits-band { position: absolute; left: 0; top: 897px; width: 839px; height: 179px; background: var(--orange);
    display: flex; flex-direction: column; align-items: center; justify-content: center; }
  .benefits-band li { list-style: none; color: var(--white); font-size: 20px; line-height: 1.5; }

  .base-rule { position: absolute; left: 0; top: 1076px; width: 839px; height: 38px; background: var(--navy); }

  .footer { position: absolute; left: 0; top: 1114px; width: 839px; height: 86px; background: var(--white); }
  .brand { position: absolute; left: 104px; top: 20px; display: flex; align-items: center; gap: 10px; }
  .brand-mark { width: 26px; height: 26px; background: var(--navy); }
  .brand-name { font-family: "Roboto", Arial, sans-serif; font-weight: 700; font-size: 34px; color: var(--navy); }
  .web { position: absolute; left: 400px; top: 14px; font-family: "Roboto", Arial, sans-serif; font-weight: 700;
    font-size: 26px; color: var(--navy); }
  .origin { position: absolute; left: 436px; top: 52px; font-family: "Roboto", Arial, sans-serif; font-weight: 700;
    font-size: 17px; color: var(--navy); }
</style>
</head>
<body>
<main class="flyer">
  <div class="top-rule"></div>
  <header class="headline-band"><h1 class="headline">Bring Back To Life Your Old Photos</h1></header>

  <section class="hero-zone"></section>

  <div class="photo photo--slides" role="img" aria-label="Scattered old slides and colour snapshots"></div>
  <div class="photo photo--old-top" role="img" aria-label="Sepia photo of a boy in front of a house"></div>
  <div class="photo photo--portraits" role="img" aria-label="Stack of vintage black and white portraits"></div>
  <div class="photo photo--film" role="img" aria-label="Curled strip of film negatives"></div>
  <div class="photo photo--children" role="img" aria-label="Two babies in Santa hats looking at a laptop"></div>

  <p class="service-line">Photo, Slide<br>and Negative Scanning</p>

  <div class="offer-count">500</div>
  <div class="offer-band"><span>Photos Scanned</span></div>
  <div class="price-band"><span>For Only</span></div>
  <div class="price"><small>$</small>50</div>

  <p class="gift-line">Ideal Christmas<br>Present For<br>All The Family!</p>

  <p class="pickup-note">Pickup &amp; Drop off<br>Service available in<br>Perth North<br>for only <em>$15.00</em></p>

  <ul class="benefits-band">
    <li>Don’t keep your Treasured old photos under the bed anymore</li>
    <li>Breath new life into them</li>
    <li>Preserve them for life</li>
    <li>Digitize them and watch on your TV or Computer anytime</li>
    <li>Protect them from Fire, Flood or Damage</li>
  </ul>

  <div class="base-rule"></div>

  <footer class="footer">
    <div class="brand"><span class="brand-mark"></span><span class="brand-name">RetroDigi</span></div>
    <div class="web">www.retrodigi.com.au</div>
    <div class="origin">100% WA Owned and Operated</div>
  </footer>
</main>
</body>
</html>
```